We Buy Houses Website

Looking for a highly motivated and skillfull designer to design and code me a "we Buy Houses" type website. I have a potential logo, but if you think you can make a BETTER one, please do try and incorporate it in your template. I am looking for creativity, professionalism, simple yet elegant. I will need a simple form on the front of the template along with pictures I provide you of recent houses I have bought. Look at these sites for examples of the layout of the website:

http://www.brickvalehomes.example/
http://www.petrafixeshouses.example/
http://www.quickpropertyexitnow.example/

If you make me a design that blows me away, and you are dependable, you will become part of my team and in charge of the web aspect which will include designing, updating, any and all graphics and logo work, SEO, coding. If you have skills in all of these areas please make me a design and lets do business!! The name of the website will be "Lurt Takes Homes" at LurtTakesHomes.example

I have uploaded some pictures of houses that we have done, please feel free to incorporate this into the banner or the design, etc. I want them to know we buy houses in ANY condition, as is, cash, can close immediately so they can get on with their life. We have many options to help them find a solution to whatever problem they have. We are in the business of helping people.

Target Market(s)

People looking to sell their houses
people facing foreclosure, bankruptcy, death in the family, divorce, anyone that we can help
people with ugly houses that need a lot of repair

Industry/Entity Type

Business

Font styles to use
Serif
Sans Serif

Colors

Designer to choose colors to be used in the design.

Requirements
Must have
• must have a simple form on the front of the page, preferrably near the banner, with the few required fields to help someone get started putting in their interest to sell their house, view the 2 websites i put as examples to see what kind of fields it should have.

My phone number (555) 482-1937 along with a Lurt Takes Homes logo, clean simple and elegant and professional. I want a nice color scheme that is not white but professional and has a wow factor.

```html
<!DOCTYPE html>
<html lang="en">
<head>
<meta charset="utf-8">
<title>Lurt Takes Homes</title>
<link href="https://fonts.googleapis.com/css2?family=Roboto+Slab:wght@400;700&family=Roboto:wght@400;500;700&family=Noto+Serif:wght@400;700&display=swap" rel="stylesheet">
<style>
:root{
  --green:#8fc31f;
  --green-dark:#6f9d10;
  --charcoal:#2e302f;
  --charcoal-deep:#232524;
  --ink:#2b2b2b;
  --muted:#666;
  --line:#d9d9d9;
  --white:#fff;
}
*{box-sizing:border-box;margin:0;padding:0}
html,body{width:1200px;height:2885px;overflow:hidden;background:#fff}
body{font-family:'Noto Serif',serif;color:var(--ink);position:relative}
.page{position:relative;width:1200px;height:2885px;overflow:hidden}
.abs{position:absolute}
/* top bar */
.topbar{left:0;top:0;width:1200px;height:42px;background:var(--charcoal-deep);font-family:'Roboto',sans-serif;font-size:12px;color:#bbb}
.topbar .mail{position:absolute;left:173px;top:13px}
.topbar .links{position:absolute;left:696px;top:13px;display:flex;gap:22px}
.topbar .soc{position:absolute;left:826px;top:12px;display:flex;gap:28px}
.topbar .soc i{display:block;width:16px;height:16px;border-radius:50%;background:#777}
/* header */
.header{left:0;top:42px;width:1200px;height:100px;background:var(--charcoal)}
.brand{position:absolute;left:173px;top:22px;display:flex;align-items:center;gap:10px;font-family:'Roboto Slab',serif;font-weight:700;font-size:20px;color:var(--green)}
.brand .mark{width:22px;height:22px;background:var(--green)}
.phone{position:absolute;left:827px;top:14px;display:flex;align-items:center;gap:12px;font-family:'Roboto',sans-serif;font-weight:700;font-size:25px;color:var(--green)}
.nav{position:absolute;left:410px;top:70px;display:flex;gap:0;font-family:'Roboto',sans-serif;font-size:12.5px;font-weight:500;color:#eee;text-transform:uppercase}
.nav a{color:inherit;text-decoration:none;padding:0 11px 9px;border-bottom:3px solid transparent}
.nav a.active{color:var(--green);border-color:var(--green)}
/* hero */
.hero{left:0;top:142px;width:1200px;height:429px;background:linear-gradient(180deg,#3f63a8 0%,#7a8fb8 38%,#8a8478 55%,#6d6a5e 70%,#4e6a2c 100%)}
.before{left:192px;top:394px;width:289px;height:154px;border:4px solid #fff;background:linear-gradient(180deg,#9fb1c9 0%,#b9ab95 55%,#6f7a4a 100%)}
.before-tag{left:421px;top:522px;background:var(--green);color:#fff;font-family:'Roboto',sans-serif;font-size:13px;padding:3px 10px}
.offer{left:756px;top:208px;width:273px;height:369px;background:var(--charcoal-deep)}
.offer .head{height:75px;background:var(--green);padding:11px 0 0 38px;font-family:'Roboto Slab',serif;color:#1f1f1f;line-height:1}
.offer .head b{display:block;font-size:27px}
.offer .head span{display:block;font-size:22px;margin-top:2px}
.field{position:absolute;left:17px;width:242px;height:29px;border:1px solid #666;color:#ccc;font-family:'Roboto',sans-serif;font-size:13px;padding:6px 8px;background:#2a2c2b}
.field.half{width:100px}
.caret{position:absolute;right:8px;top:11px;border:5px solid transparent;border-top-color:#ccc}
.submit{position:absolute;left:36px;top:334px;width:202px;height:36px;background:linear-gradient(#a9d82e,#7db012);color:#111;font-family:'Roboto',sans-serif;font-weight:700;font-size:17px;text-align:center;line-height:36px}
.offer-tab{left:724px;top:571px;width:340px;height:26px;background:#3a3c3b;clip-path:polygon(0 0,100% 0,92% 100%,8% 100%)}
/* steps */
.step-label{font-family:'Roboto',sans-serif;font-size:13px;color:#333;text-align:center}
.step{width:104px;height:104px;border-radius:50%;display:flex;align-items:center;justify-content:center}
.step.dark{background:#2b2d2c}
.step.green{background:var(--green)}
.hatch{height:10px;background:repeating-linear-gradient(135deg,#ccc 0 1px,transparent 1px 4px)}
.intro{left:169px;top:907px;width:855px;font-size:11.5px;line-height:16.4px;color:#444}
/* section heads */
.shead{font-family:'Roboto Slab',serif;font-weight:700;font-size:25px;text-transform:uppercase;display:flex;align-items:center;gap:14px}
.shead.green{color:var(--green)}
.arrows{display:flex;gap:6px}
.arrows i{display:block;width:22px;height:22px;border-radius:50%;background:#222;position:relative}
.arrows i::after{content:"";position:absolute;left:8px;top:7px;width:6px;height:6px;border-left:2px solid #fff;border-bottom:2px solid #fff;transform:rotate(45deg)}
.arrows i.next::after{left:6px;transform:rotate(-135deg)}
/* cards */
.card{width:273px}
.card .photo{height:186px;position:relative}
.card .sale{position:absolute;right:0;top:0;background:#222;color:#fff;font-family:'Roboto',sans-serif;font-size:13px;padding:5px 10px}
.card .kind{position:absolute;right:0;top:40px;background:var(--green);color:#fff;font-family:'Roboto',sans-serif;font-size:13px;padding:4px 8px}
.card h3{font-family:'Roboto Slab',serif;font-size:16px;margin:10px 0 14px}
.specs{font-family:'Roboto',sans-serif;font-size:11.5px;color:#333;border-top:1px dotted #aaa;border-bottom:1px dotted #aaa;padding:6px 0;line-height:22px}
.specs span{margin-right:12px}
.specs span::before{content:"";display:inline-block;width:8px;height:8px;background:#444;margin-right:5px;border-radius:2px}
.btn-detail{display:block;margin:14px auto 0;width:155px;height:34px;border:1px solid #ccc;text-align:center;line-height:32px;font-family:'Roboto',sans-serif;font-size:14px;color:#777}
/* services */
.services{left:0;top:1523px;width:1200px;height:433px;background:linear-gradient(180deg,#3a3835 0%,#4a4a4c 40%,#2e3a4e 75%,#273248 100%)}
.svc{width:235px}
.svc h4{font-family:'Roboto',sans-serif;font-weight:400;font-size:15px;color:var(--green);display:flex;align-items:flex-start;gap:8px;line-height:18px}
.svc h4 svg{flex:none}
.svc p{font-size:11.5px;line-height:15.5px;color:#fff;margin-top:10px}
/* testimonials */
.avatar{left:175px;top:2085px;width:106px;height:106px;border-radius:50%;border:4px solid #ddd;background:linear-gradient(180deg,#b9b4ae,#5a5d66)}
.quote{left:307px;top:2085px;width:300px;font-size:11.5px;line-height:16px;color:#444}
.who{left:514px;top:2218px;font-size:12px;color:var(--green);font-family:'Roboto',sans-serif}
.dots{left:377px;top:2258px;display:flex;gap:5px}
.dots i{width:10px;height:10px;border-radius:50%;background:#222}
.dots i:first-child{background:var(--green)}
.tabs{left:652px;top:2060px;display:flex;gap:4px;font-family:'Roboto',sans-serif;font-size:12px}
.tabs span{padding:5px 14px;background:#e6e6e6;border:1px solid #ccc;color:#444}
.tabs span.on{background:#fff;color:var(--green);border-bottom-color:#fff;border-top:2px solid var(--green)}
.tabbox{left:637px;top:2085px;width:391px;height:176px;border:1px solid #ccc;padding:20px 20px;font-size:11.5px;line-height:16px;color:#333}
/* partners */
.partner{display:flex;align-items:center;justify-content:center;width:150px;height:80px}
/* footer */
.footer{left:0;top:2506px;width:1200px;height:336px;background:#333534;color:#ddd}
.fhead{font-family:'Roboto',sans-serif;font-size:16px;color:#fff;border-bottom:1px solid #444;padding-bottom:8px}
.fprop{display:flex;gap:12px;margin-top:14px;font-family:'Roboto',sans-serif;font-size:12px;line-height:16px}
.fprop .th{width:62px;height:58px;flex:none}
.fprop small{display:block;color:#888;margin-top:8px}
.cat{font-family:'Roboto',sans-serif;font-size:12.5px;color:#ccc;border-bottom:1px solid #444;padding:7px 0 8px}
.contact{font-family:'Roboto',sans-serif;font-size:12px;color:#aaa;line-height:19px}
.contact.one{white-space:nowrap;font-size:11px}
.fsoc{display:flex;gap:7px}
.fsoc i{width:20px;height:20px;border-radius:50%;background:#555}
.bottombar{left:0;top:2842px;width:1200px;height:43px;background:#232524;font-family:'Roboto',sans-serif;font-size:11px;color:#888}
</style>
</head>
<body>
<div class="page">

<div class="abs topbar">
  <span class="mail">&#9993;&nbsp; info@lurttakeshomes.example</span>
  <div class="links"><span>Login</span><span>Register</span></div>
  <div class="soc"><i></i><i></i><i></i><i></i><i></i></div>
</div>

<header class="abs header">
  <div class="brand"><span class="mark"></span>LURT TAKES HOMES</div>
  <div class="phone">
    <svg width="36" height="36" viewBox="0 0 36 36"><circle cx="18" cy="18" r="16" fill="none" stroke="#bbb" stroke-width="2"/><path d="M10 15c0-4 16-4 16 0l-3 2c-2-2-8-2-10 0zM12 18h12l2 8H10z" fill="#bbb"/></svg>
    (555) 482-1937
  </div>
  <nav class="nav">
    <a class="active">Home</a><a>Sell My House Fast</a><a>How It Works</a><a>About Me</a><a>Recent Projects</a><a>Investors</a>
  </nav>
</header>

<section class="abs hero" role="img" aria-label="Photo of a renovated single-storey house with a garage and front lawn"></section>
<div class="abs before" role="img" aria-label="Photo of the same house before renovation"></div>
<div class="abs before-tag">Before</div>

<div class="abs offer-tab"></div>
<form class="abs offer">
  <div class="head"><b>GET AN OFFER</b><span>ON YOUR HOUSE</span></div>
  <div class="field" style="top:96px">Name</div>
  <div class="field" style="top:131px">Phone Number</div>
  <div class="field" style="top:167px">Your Email</div>
  <div class="field" style="top:203px">Property Address</div>
  <div class="field half" style="top:239px">USA<span class="caret"></span></div>
  <div class="field" style="top:239px;left:125px;width:134px">City<span class="caret"></span></div>
  <div class="field" style="top:275px">Zip Code</div>
  <div class="submit">SUBMIT</div>
</form>

<svg class="abs" style="left:250px;top:625px" width="700" height="160" viewBox="0 0 700 160">
  <g fill="none" stroke="#aaa" stroke-width="1.5" stroke-dasharray="4 4">
    <path d="M45 55 Q120 20 205 60"/>
    <path d="M265 135 Q350 140 415 100"/>
    <path d="M490 55 Q580 20 660 60"/>
  </g>
  <g fill="#aaa"><path d="M205 60l-9-2 5-6z"/><path d="M415 100l-3 9-5-5z"/><path d="M660 60l-9-2 5-6z"/></g>
</svg>
<div class="abs step-label" style="left:185px;top:626px">1. Fill In The Form</div>
<div class="abs step-label" style="left:630px;top:626px">3. Find A Solution</div>
<div class="abs step-label" style="left:405px;top:797px;width:140px">2. Get A Call Within<br>24 Hours</div>
<div class="abs step-label" style="left:870px;top:801px">4. Go On With Your Life</div>
<div class="abs step dark" style="left:206px;top:663px"><svg width="44" height="44" viewBox="0 0 44 44" fill="none" stroke="#fff" stroke-width="3"><rect x="8" y="7" width="26" height="32" rx="2"/><path d="M16 4h10v6H16zM14 20h12M14 27h8M34 18l-10 14-4 1 1-4 10-14z"/></svg></div>
<div class="abs step green" style="left:423px;top:663px"><svg width="44" height="44" viewBox="0 0 44 44" fill="none" stroke="#fff" stroke-width="3"><path d="M12 8l6 7-4 4c2 5 6 9 11 11l4-4 7 6-4 6C19 38 6 25 6 12z"/><path d="M26 6l10 10M26 6v8M26 6h8" /></svg></div>
<div class="abs step dark" style="left:661px;top:663px"><svg width="44" height="44" viewBox="0 0 44 44" fill="#fff"><path d="M8 14h9a4 4 0 1 1 8 0h9v9a4 4 0 1 0 0 8v6H25a4 4 0 1 0-8 0H8v-9a4 4 0 1 0 0-8z"/></svg></div>
<div class="abs step green" style="left:890px;top:663px"><svg width="44" height="44" viewBox="0 0 44 44" fill="none" stroke="#fff" stroke-width="3"><path d="M16 6h12l-4 7h-4z"/><path d="M18 13c-8 4-12 11-12 17 0 6 6 9 16 9s16-3 16-9c0-6-4-13-12-17z"/><path d="M25 21c-1-2-6-2-6 1s6 2 6 5-5 3-6 1M22 18v3M22 29v3"/></svg></div>
<div class="abs hatch" style="left:169px;top:864px;width:860px"></div>

<p class="abs intro">Lorem ipsum dolor sit amet, consectetuer adipiscing elit, sed diam nonummy nibh euismod tincidunt utreet dolore magna aliquam erat volutpat. Ut wisi enim ad minim veniam, quis nostrud exerci tation ullamcorper suscipit lobortis nisl ut aliquip ex ea commodo consequat. Duis autem vel eum iriure dolor in hendrerit in vulputate velit esse molestie consequat, vel illum dolore eu fet nulla facilisis at vero eros et accumsan et iusto odio dignissim qui blandit praesent luptatum zzril delenit augue duis dolore te feugait nulla facilisiLorem ipsum dolor sit amet, consectetuer adipiscing elit, sed diam nonummy nibh euismod tincidunt utreet dolore magna aliquam erat volutpat. Ut wisi enim ad minim veniam, quis nostrud exerci tation ullamcorper suscipit lobortis nisl ut aliquip ex ea commodo consequat. Duis autem vel eum iriure dolor in hendrerit in vulputate velit esse molestie consequat, vel illum dolore eu fet nulla facilisis at vero eros et accumsan et iusto odio dignissim qui blandit praesent luptatum zzril delenit augue duis dolore te feugait nulla facilisi.</p>

<div class="abs shead green" style="left:172px;top:1080px;width:855px">Recent Projects<span class="hatch" style="flex:1"></span><span class="arrows"><i></i><i class="next"></i></span></div>

<article class="abs card" style="left:169px;top:1154px">
  <div class="photo" role="img" aria-label="Photo of a renovated kitchen with dark wood cabinets" style="background:linear-gradient(160deg,#8a6a4a,#3e2c1f 70%,#c9b79c)"><span class="sale">Sale</span><span class="kind">Office</span></div>
  <h3>Central Park View</h3>
  <div class="specs"><span>Area : 65000/m²</span><span>Beds : 4</span><span>Baths : 3</span><br><span>Floors : 5</span><span>Garage : 1</span></div>
  <span class="btn-detail">VIEW DETAIL</span>
</article>
<article class="abs card" style="left:458px;top:1154px">
  <div class="photo" role="img" aria-label="Photo of a renovated bathroom with vanity and mirror" style="background:linear-gradient(160deg,#6b4b32,#a88b6c 55%,#d7d2c8)"><span class="sale">Sale</span><span class="kind">Farm House</span></div>
  <h3>The Urban Life</h3>
  <div class="specs"><span>Area : 45000/m²</span><span>Beds : 2</span><span>Baths : 2</span><br><span>Floors : 2</span><span>Garage : 3</span></div>
  <span class="btn-detail">VIEW DETAIL</span>
</article>
<article class="abs card" style="left:748px;top:1154px">
  <div class="photo" role="img" aria-label="Photo of a renovated kitchen with white appliances" style="background:linear-gradient(160deg,#5d4330,#8a6d52 55%,#cfc8bd)"><span class="sale">Sale</span><span class="kind">Commercial</span></div>
  <h3>House On The Beach</h3>
  <div class="specs"><span>Area : 67000/m²</span><span>Beds : 4</span><span>Baths : 3</span><br><span>Floors : 5</span><span>Garage : 1</span></div>
  <span class="btn-detail">VIEW DETAIL</span>
</article>

<section class="abs services" role="img" aria-label="Background photo of snow-capped mountains at dusk"></section>
<div class="abs svc" style="left:169px;top:1612px"><h4><svg width="20" height="20" viewBox="0 0 20 20" fill="none" stroke="#8fc31f" stroke-width="2"><circle cx="10" cy="10" r="4"/><circle cx="10" cy="10" r="8" stroke-dasharray="3 2"/></svg>Agency Leasing</h4><p>Lorem ipsum dolor sit amet, consectetuer adipiscing elit. Vivamus ac luctus ligula. Phasellus a ligula blandit</p></div>
<div class="abs svc" style="left:477px;top:1612px"><h4><svg width="20" height="20" viewBox="0 0 20 20" fill="#8fc31f"><path d="M10 2a8 8 0 1 0 0 16c2 0 2-2 1-3s0-3 2-3h3c2 0 2-2 2-3 0-4-4-7-8-7z"/></svg>Property and Asset Management</h4><p>Lorem ipsum dolor sit amet, consectetuer adipiscing elit. Vivamus ac luctus ligula. Phasellus a ligula blandit</p></div>
<div class="abs svc" style="left:794px;top:1612px"><h4><svg width="20" height="20" viewBox="0 0 20 20" fill="#8fc31f"><path d="M7 2h6v2h-1v5l6 9H2l6-9V4H7z"/></svg>Real Estate Intelligence Service</h4><p>Lorem ipsum dolor sit amet, consectetuer adipiscing elit. Vivamus ac luctus ligula. Phasellus a ligula blandit</p></div>
<div class="abs svc" style="left:169px;top:1766px"><h4><svg width="20" height="20" viewBox="0 0 20 20" fill="none" stroke="#8fc31f" stroke-width="4"><path d="M4 2v8a6 6 0 0 0 12 0V2"/></svg>Lease Administration</h4><p>Lorem ipsum dolor sit amet, consectetuer adipiscing elit. Vivamus ac luctus ligula. Phasellus a ligula blandit</p></div>
<div class="abs svc" style="left:477px;top:1766px"><h4><svg width="20" height="20" viewBox="0 0 20 20" fill="none" stroke="#8fc31f" stroke-width="2.5"><path d="M3 17l9-9M11 3l6 6-3 3-6-6z"/></svg>Transaction Management</h4><p>Lorem ipsum dolor sit amet, consectetuer adipiscing elit. Vivamus ac luctus ligula. Phasellus a ligula blandit</p></div>
<div class="abs svc" style="left:794px;top:1766px"><h4><svg width="20" height="20" viewBox="0 0 20 20" fill="#8fc31f"><path d="M5 2h10v5a5 5 0 0 1-10 0zM9 12h2v4h3v2H6v-2h3z"/></svg>Strategic Consulting</h4><p>Lorem ipsum dolor sit amet, consectetuer adipiscing elit. Vivamus ac luctus ligula. Phasellus a ligula blandit</p></div>

<div class="abs shead" style="left:172px;top:2015px;width:420px;font-size:23px">Testimonials<span class="hatch" style="flex:1"></span></div>
<div class="abs avatar" role="img" aria-label="Portrait photo of a client"></div>
<p class="abs quote">Nunc at pretium est curabitur commodo leac est venenatis egestas sed aliquet augueveilt. Lorem ipsum dolor sit amet, consectetur adipiscing elit. Vivamus ac luctus ligula. Phasellus a ligula blandit</p>
<div class="abs who">– John Doe</div>
<div class="abs dots"><i></i><i></i><i></i></div>

<div class="abs shead" style="left:637px;top:2015px;font-size:23px">Benefits From Property</div>
<div class="abs tabs"><span class="on">Pretium</span><span>Luctus</span><span>Ligula</span></div>
<div class="abs tabbox">Pretium est curabitur commodo leac est venenatis egestas sed aliquet augueveilt. Lorem ipsum dolor sit amet, consectetur adipiscing elit. Vivamus ac luctus ligula. Phasellus a ligula blandit Pretium est curabitur commodo leac est venenatis egestas sed aliquet augueveilt. Lorem ipsum dolor sit amet, consectetur adipiscing elit. Vivamus ac luctus ligula. Phasellus a ligula blandit</div>

<div class="abs shead green" style="left:172px;top:2322px;width:855px">Our Partners<span class="hatch" style="flex:1"></span><span class="arrows"><i></i><i class="next"></i></span></div>
<div class="abs partner" style="left:175px;top:2393px"><svg width="60" height="60"><circle cx="30" cy="30" r="26" fill="#5aa9c9"/></svg></div>
<div class="abs partner" style="left:403px;top:2393px"><svg width="60" height="60"><circle cx="30" cy="30" r="26" fill="#e7a64a"/></svg></div>
<div class="abs partner" style="left:643px;top:2393px"><svg width="60" height="60"><circle cx="30" cy="30" r="26" fill="#d77a7a"/></svg></div>
<div class="abs partner" style="left:858px;top:2393px"><svg width="60" height="60"><circle cx="30" cy="30" r="26" fill="#4f7fb8"/></svg></div>

<footer class="abs footer">
  <div class="abs" style="left:171px;top:40px;width:190px">
    <div class="fhead">Properties</div>
    <div class="fprop"><div class="th" role="img" aria-label="Thumbnail photo of a villa" style="background:linear-gradient(#7aa0c8,#6b7a4a)"></div><div>Luxury Villa In Bego Park<small>$ 45000</small></div></div>
    <div class="fprop"><div class="th" role="img" aria-label="Thumbnail photo of a house" style="background:linear-gradient(#9ab3cf,#7b8a5a)"></div><div>Lovelace Road Greenfield<small>$ 45000</small></div></div>
    <div class="fprop"><div class="th" role="img" aria-label="Thumbnail photo of a house by the water" style="background:linear-gradient(#5f93c9,#3e6b8f)"></div><div>Land In Central Park<small>$ 45000</small></div></div>
  </div>
  <div class="abs" style="left:388px;top:40px;width:190px">
    <div class="fhead">Photos from Snapfolio</div>
    <div style="display:grid;grid-template-columns:repeat(3,58px);gap:5px;margin-top:14px">
      <div role="img" aria-label="Gallery photo" style="height:58px;background:#8a7a6a"></div>
      <div role="img" aria-label="Gallery photo" style="height:58px;background:#9a5a3a"></div>
      <div role="img" aria-label="Gallery photo" style="height:58px;background:#6a7a8a"></div>
      <div role="img" aria-label="Gallery photo" style="height:58px;background:#7a6a5a"></div>
      <div role="img" aria-label="Gallery photo" style="height:58px;background:#4a4a5a"></div>
      <div role="img" aria-label="Gallery photo" style="height:58px;background:#3a3a6a"></div>
      <div role="img" aria-label="Gallery photo" style="height:58px;background:#8a6a4a"></div>
      <div role="img" aria-label="Gallery photo" style="height:58px;background:#6a5a4a"></div>
      <div role="img" aria-label="Gallery photo" style="height:58px;background:#9a8a7a"></div>
    </div>
  </div>
  <div class="abs" style="left:602px;top:40px;width:160px">
    <div class="fhead">Categories</div>
    <div class="cat">Apartment</div><div class="cat">Audio</div><div class="cat">Cottage</div><div class="cat">Magazine</div><div class="cat">Retail</div><div class="cat">Technical</div><div class="cat">Video</div>
  </div>
  <div class="abs" style="left:827px;top:40px;width:215px">
    <div class="fhead">Contact Info</div>
    <p class="contact" style="margin-top:14px">48 Alder Row, Fenwick Lane,<br>Marlow Bay, Exampleshire</p>
    <p class="contact" style="margin-top:12px">&#9990;&nbsp; Phone : 555-0148-2210</p>
    <p class="contact one" style="margin-top:6px">&#9993;&nbsp; Email : hello@lurttakeshomes.example</p>
    <div class="fsoc" style="margin-top:16px"><i></i><i></i><i></i><i></i><i></i></div>
    <div style="margin-top:26px;display:flex;align-items:center;gap:8px;font-family:'Roboto Slab',serif;font-weight:700;font-size:13px;color:#666"><span style="width:12px;height:12px;background:#666"></span>LURT TAKES HOMES</div>
  </div>
</footer>
<div class="abs bottombar">
  <span style="position:absolute;left:177px;top:15px">Copyright © 2014 LurtTakesHomes.example All Rights Reserved.</span>
  <svg style="position:absolute;left:953px;top:10px" width="22" height="22" viewBox="0 0 22 22" fill="none" stroke="#aaa" stroke-width="1.5"><circle cx="11" cy="11" r="9"/><path d="M7 13l4-4 4 4"/></svg>
</div>

</div>
</body>
</html>
```